Brenmor Water - 500ml

to create a water bottle packaging similar to Brume Claire design. Bottle should be blue similar to NORTH KIND but change the design/logo to Brenmor. Wording should be similar just different design and logo. Thanks.

Colors
0054AA
0677BA
7BADD7
CADEEF
E8F1F8

Requirements
Must have
• Bottle must not be in plastic bottles. They are made in a carton instead - see NORTH KIND for reference.

```html
<!DOCTYPE html>
<html lang="en">
<head>
<meta charset="UTF-8">
<title>Brenmor Water – 500 ml carton</title>
<link rel="stylesheet" href="https://fonts.googleapis.com/css2?family=Oswald:wght@400;600;700&family=Roboto+Condensed:wght@400;700&display=swap">
<style>
  :root {
    --backdrop: #e8f1f8;
    --carton-blue: #29a8e0;
    --carton-blue-deep: #0677ba;
    --navy: #1e2a5e;
    --pale-blue: #7badd7;
    --ice: #cadeef;
    --white: #ffffff;
  }
  * { box-sizing: border-box; margin: 0; padding: 0; }
  html, body {
    width: 843px;
    height: 1200px;
    overflow: hidden;
    background: var(--backdrop);
  }
  .canvas {
    position: relative;
    width: 843px;
    height: 1200px;
  }
  .carton-front {
    position: absolute;
    left: 231px;
    top: 30px;
    width: 380px;
    height: 1140px;
    background: var(--carton-blue);
    overflow: hidden;
  }
  .brand {
    position: absolute;
    top: 108px;
    left: 0;
    width: 100%;
    text-align: center;
  }
  .brand-name {
    font-family: "Oswald", sans-serif;
    font-weight: 700;
    font-size: 62px;
    line-height: 1;
    letter-spacing: 1px;
    color: var(--navy);
  }
  .brand-tagline {
    margin-top: 8px;
    font-family: "Roboto Condensed", sans-serif;
    font-weight: 400;
    font-size: 11px;
    letter-spacing: 1.5px;
    color: var(--navy);
  }
  .product-band {
    position: absolute;
    top: 515px;
    left: 0;
    width: 100%;
    height: 318px;
    background: var(--navy);
    display: flex;
    align-items: center;
    padding-left: 38px;
    gap: 10px;
  }
  .product-band .vertical {
    writing-mode: vertical-rl;
    transform: rotate(180deg);
    font-family: "Oswald", sans-serif;
    line-height: 1;
  }
  .product-claim {
    font-weight: 400;
    font-size: 27px;
    letter-spacing: 5px;
    color: var(--ice);
  }
  .product-name {
    font-weight: 700;
    font-size: 112px;
    letter-spacing: 2px;
    color: var(--white);
  }
  .carton-footer {
    position: absolute;
    left: 30px;
    right: 26px;
    bottom: 92px;
    display: flex;
    justify-content: space-between;
    align-items: flex-end;
    color: var(--navy);
  }
  .sustainability-note {
    font-family: "Roboto Condensed", sans-serif;
    font-weight: 400;
    font-size: 15px;
    line-height: 1.3;
  }
  .volume {
    font-family: "Oswald", sans-serif;
    font-weight: 600;
    font-size: 30px;
    line-height: 1;
  }
</style>
</head>
<body>
  <main class="canvas">
    <section class="carton-front">
      <header class="brand">
        <h1 class="brand-name">Brenmor</h1>
        <p class="brand-tagline">PURE NATURAL SPRING WATER</p>
      </header>

      <div class="product-band">
        <span class="vertical product-claim">100% SPRING</span>
        <span class="vertical product-name">WATER</span>
      </div>

      <footer class="carton-footer">
        <p class="sustainability-note">Sustainably sourced water<br>in a plant based carton</p>
        <p class="volume">500 ML</p>
      </footer>
    </section>
  </main>
</body>
</html>
```